Ashcombe Card Design

We need an updated business card. We have been in business for 25 years providing environmental remediation services like asbestos abatement, mold remediation, emergency response and property restoration. Please see the logo attached, design of our shirt, and old business card. We need something fresh and new and list the services we offer...asbestos abatement, mold remediation, emergency response and property restoration.

Industry/Entity Type

Business

Contact Information for Business Card

Ashcombe Companies
417 Brindle Street
Fernvale, NV 19388
Gavin Porter
VP Business Development
gporter@ashenvo.com
www.ashcoz.com
Cell: 484-555-0186
Phone: 610-555-0142
Fax: 610-555-0143

Requirements
Must have
• logo should be incorporated w/ list of services

```html
<!DOCTYPE html>
<html lang="en">
<head>
<meta charset="utf-8">
<title>Ashcombe Companies – Business Card</title>
<link rel="stylesheet" href="https://fonts.googleapis.com/css2?family=Didact+Gothic&family=Mulish:wght@800&display=swap">
<style>
  :root {
    --brand-blue: #3a5ba8;
    --bullet-blue: #1f8fd6;
    --ink: #141414;
    --card: #ffffff;
    --backdrop: #e9e6e1;
  }
  * { margin: 0; padding: 0; box-sizing: border-box; }
  html, body { width: 1200px; height: 1200px; overflow: hidden; }
  body {
    background: var(--backdrop);
    font-family: "Didact Gothic", "Century Gothic", sans-serif;
    color: var(--ink);
  }
  .card {
    position: absolute;
    left: 75px; top: 300px;
    width: 1050px; height: 600px;
    background: var(--card);
    box-shadow: 0 6px 24px rgba(0,0,0,.18);
    overflow: hidden;
  }
  .brand-mark {
    position: absolute;
    left: 50px; top: 60px;
    width: 250px; height: 250px;
    border-radius: 50%;
    background: var(--brand-blue);
  }
  .company-name {
    position: absolute;
    left: 330px; top: 58px;
    font-family: "Mulish", "Century Gothic", sans-serif;
    font-weight: 800;
    font-size: 52px;
    letter-spacing: 1px;
    text-transform: uppercase;
    color: var(--brand-blue);
    white-space: nowrap;
  }
  .contact-list {
    position: absolute;
    right: 36px; top: 168px;
    list-style: none;
    text-align: right;
  }
  .contact-list li {
    display: flex;
    justify-content: flex-end;
    align-items: center;
    gap: 10px;
    font-size: 23px;
    line-height: 34px;
    height: 37px;
    white-space: nowrap;
  }
  .contact-list svg { width: 26px; height: 26px; flex: none; }
  .person {
    position: absolute;
    left: 50px; top: 388px;
  }
  .person-name { font-size: 42px; line-height: 1.1; font-weight: 400; }
  .person-title { font-size: 22px; color: var(--brand-blue); }
  .services {
    position: absolute;
    left: 26px; right: 26px; top: 500px;
    display: flex;
    justify-content: space-between;
    list-style: none;
    font-size: 22px;
    white-space: nowrap;
  }
  .services li::before {
    content: "•";
    color: var(--bullet-blue);
    margin-right: 4px;
  }
  .services li:last-child::after {
    content: "•";
    color: var(--bullet-blue);
    margin-left: 4px;
  }
  .base-band {
    position: absolute;
    left: 0; right: 0; bottom: 0;
    height: 56px;
    background: var(--brand-blue);
  }
</style>
</head>
<body>
<article class="card">
  <div class="brand-mark" aria-hidden="true"></div>
  <h1 class="company-name">Ashcombe Companies</h1>

  <ul class="contact-list">
    <li>gporter@ashenvo.com
      <svg viewBox="0 0 24 24" aria-hidden="true"><rect x="2" y="5" width="20" height="14" rx="1" fill="#3a5ba8"/><path d="M2 6l10 7 10-7" fill="none" stroke="#fff" stroke-width="1.6"/></svg>
    </li>
    <li>www.ashcoz.com
      <svg viewBox="0 0 24 24" aria-hidden="true"><g fill="none" stroke="#3a5ba8" stroke-width="1.6"><circle cx="12" cy="12" r="9.5"/><ellipse cx="12" cy="12" rx="4.2" ry="9.5"/><path d="M2.5 12h19M4 7h16M4 17h16"/></g></svg>
    </li>
    <li>Cell: 484-555-0186
      <svg viewBox="0 0 24 24" aria-hidden="true"><path d="M8 2c-2 1-3.5 3-3.5 6 0 6 5 12.5 10 14 1.6.4 3-.3 4-1.4l-3-3.6-2.3 1.1C11 16.5 8.8 12.5 8.6 9.6l2.3-1L8 2z" fill="#3a5ba8"/></svg>
    </li>
    <li>Phone: 610-555-0142
      <svg viewBox="0 0 24 24" aria-hidden="true"><path d="M2 9c0-3 4-5 10-5s10 2 10 5v1.5h-5V8.5H7v2H2z" fill="#3a5ba8"/><path d="M5 12h14l2 8H3z" fill="#3a5ba8"/><circle cx="12" cy="16" r="2.2" fill="#fff"/></svg>
    </li>
    <li>Fax: 610-555-0143
      <svg viewBox="0 0 24 24" aria-hidden="true"><rect x="6" y="2" width="12" height="7" fill="none" stroke="#3a5ba8" stroke-width="1.6"/><rect x="2" y="9" width="20" height="10" rx="1.5" fill="#3a5ba8"/><rect x="6" y="15" width="12" height="7" fill="#fff" stroke="#3a5ba8" stroke-width="1.6"/></svg>
    </li>
    <li class="address">417 Brindle Street Fernvale, NV 19388
      <svg viewBox="0 0 24 24" aria-hidden="true"><path d="M12 1.5a7.5 7.5 0 0 0-7.5 7.5c0 5.6 7.5 13.5 7.5 13.5S19.5 14.6 19.5 9A7.5 7.5 0 0 0 12 1.5z" fill="#3a5ba8"/><circle cx="12" cy="9" r="3" fill="#fff"/></svg>
    </li>
  </ul>

  <div class="person">
    <h2 class="person-name">Gavin Porter</h2>
    <p class="person-title">VP Business Development</p>
  </div>

  <ul class="services">
    <li>Emergency Response</li>
    <li>Mold Remediation</li>
    <li>Asbestos Abatement</li>
    <li>Property Restoration</li>
  </ul>

  <div class="base-band"></div>
</article>
</body>
</html>
```